Tea bag packaging design for VELIRAN

Hello. I am creating a green tea and soybean tea, and I am looking for packaging designs. I will attach some designs I like and our current VELIRAN logo. Feel free to follow the designs or create something of your own.

Package size is 200 (W) x 290(L) mm

The package is a white aluminum package so it can accommodate a wide range of colors. We don't want to pay a ton in printing so 5 colors or less is nice. But we will make exceptions for something more colorful if it's well done.

Target Market(s)

Women and Men in 30s-40s

Industry/Entity Type

food and beverage

Font styles to use
Sans Serif
Other font styles liked:
• red hat is the font of the logo

Requirements
Must have
• clean, simple, but bold design
Nice to have
• images of soybeans and green tea leaves on the package

```html
<!DOCTYPE html>
<html lang="en">
<head>
<meta charset="utf-8">
<title>VELIRAN Premium Tea Packaging</title>
<link rel="stylesheet" href="https://fonts.googleapis.com/css2?family=Red+Hat+Display:wght@500;700;800;900&display=swap">
<style>
  :root {
    --stage: #545b40;
    --green-deep: #0f2a04;
    --green-dark: #153205;
    --green-mid: #4f9a1c;
    --green-bright: #8cc43a;
    --green-lime: #a8d046;
    --green-ink: #1c3608;
    --brown-top: #b0532a;
    --brown-deep: #7c3614;
    --brown-ink: #5a2a12;
    --cream: #f7ecd6;
    --cream-warm: #f8d9a8;
    --orange-soft: #f3a95a;
    --soy-light: #f7e2ad;
    --soy-ink: #3b2b1f;
    --white: #ffffff;
    --badge-green: #2e8a2c;
    --badge-dark: #143a2a;
  }
  * { margin: 0; padding: 0; box-sizing: border-box; }
  html, body {
    width: 777px; height: 1200px; overflow: hidden;
    background: var(--stage);
    font-family: "Red Hat Display", sans-serif;
  }
  .canvas { position: relative; width: 777px; height: 1200px; }

  .label {
    position: absolute; top: 342px; width: 355px; height: 515px;
    overflow: hidden;
    box-shadow: 0 8px 18px rgba(0,0,0,0.35);
  }
  .label--green { left: 24px; }
  .label--soy { left: 398px; }

  .label__top, .label__bottom { position: absolute; left: 0; width: 100%; }
  .label__top { top: 0; height: 280px; }
  .label__bottom { top: 280px; height: 235px; }

  .label--green .label__top { background: linear-gradient(160deg, var(--green-dark) 0%, var(--green-deep) 100%); }
  .label--green .label__bottom { background: linear-gradient(180deg, var(--green-lime) 0%, var(--green-bright) 35%, var(--green-mid) 80%, #2f7a10 100%); }
  .label--soy .label__top { background: linear-gradient(150deg, var(--brown-top) 0%, var(--brown-top) 45%, var(--brown-deep) 100%); }
  .label--soy .label__bottom { background: linear-gradient(180deg, var(--cream) 0%, var(--cream-warm) 60%, var(--orange-soft) 100%); }

  .brand {
    position: absolute; left: 40px; top: 116px;
    display: flex; flex-direction: column; align-items: center; gap: 6px;
  }
  .brand__dot { width: 34px; height: 34px; border-radius: 50%; background: var(--white); }
  .brand__name { font-size: 13px; font-weight: 800; color: var(--white); letter-spacing: 0.3px; }

  .title__kicker {
    position: absolute; left: 34px; top: 196px;
    font-size: 20px; font-weight: 700; letter-spacing: 7px;
  }
  .title__main {
    position: absolute; left: 32px; top: 214px;
    font-size: 62px; font-weight: 800; letter-spacing: -2px; line-height: 1;
  }
  .title__tea {
    position: absolute; left: 134px; top: 270px;
    font-size: 62px; font-weight: 900; letter-spacing: -2px; line-height: 1;
  }
  .label--green .title__kicker,
  .label--green .title__main { color: var(--green-lime); }
  .label--green .title__tea { color: var(--green-ink); }
  .label--soy .title__kicker { color: var(--white); left: 36px; top: 200px; }
  .label--soy .title__main { color: var(--soy-light); font-size: 50px; left: 34px; top: 226px; }
  .label--soy .title__tea { color: var(--brown-ink); left: 136px; top: 272px; }

  .art { position: absolute; border-radius: 40% 60% 45% 55%; }
  .art--leaf { left: 42px; top: 268px; width: 96px; height: 62px;
    background: radial-gradient(ellipse at 60% 45%, #62b02c 0%, #2f7a12 70%, rgba(47,122,18,0) 100%); }
  .art--soybean { left: 36px; top: 280px; width: 100px; height: 58px;
    background: radial-gradient(ellipse at 45% 50%, #f4dba6 0%, #e2bd7c 65%, rgba(226,189,124,0) 100%); }

  .claims { position: absolute; left: 33px; top: 385px; }
  .claims__headline { font-size: 20px; font-weight: 900; letter-spacing: 0.2px; }
  .claims__weight { margin-top: 6px; font-size: 12px; font-weight: 500; letter-spacing: 0.3px; }
  .label--green .claims { color: var(--white); }
  .label--soy .claims { color: var(--soy-ink); }

  .badges {
    position: absolute; left: 256px; top: 290px; width: 66px; height: 202px;
    border-radius: 33px;
    display: flex; flex-direction: column; align-items: center; justify-content: space-around;
    padding: 6px 0;
  }
  .label--green .badges { border: 1.5px solid rgba(255,255,255,0.85); }
  .label--soy .badges { border: 1.5px solid var(--brown-top); }
  .badge {
    width: 52px; height: 52px; border-radius: 50%;
    border: 4px solid var(--white);
    box-shadow: 0 0 0 1.5px var(--badge-dark);
  }
  .badge--organic { background: var(--badge-green); }
  .badge--vegan { background: var(--badge-dark); }
  .badge--fresh { background: #3d9a36; }
</style>
</head>
<body>
<main class="canvas">

  <section class="label label--green" aria-label="Premium green tea front label">
    <div class="label__top"></div>
    <div class="label__bottom"></div>
    <div class="brand">
      <span class="brand__dot"></span>
      <span class="brand__name">VELIRAN</span>
    </div>
    <p class="title__kicker">Premium</p>
    <p class="title__main">green</p>
    <div class="art art--leaf" role="img" aria-label="Fresh green tea leaves"></div>
    <p class="title__tea">tea</p>
    <div class="claims">
      <p class="claims__headline">ALL NATURAL</p>
      <p class="claims__weight">NT WT. 200 G</p>
    </div>
    <div class="badges">
      <span class="badge badge--organic"></span>
      <span class="badge badge--vegan"></span>
      <span class="badge badge--fresh"></span>
    </div>
  </section>

  <section class="label label--soy" aria-label="Premium soybean tea front label">
    <div class="label__top"></div>
    <div class="label__bottom"></div>
    <div class="brand">
      <span class="brand__dot"></span>
      <span class="brand__name">VELIRAN</span>
    </div>
    <p class="title__kicker">Premium</p>
    <p class="title__main">Soybean</p>
    <div class="art art--soybean" role="img" aria-label="Soybeans with a green leaf"></div>
    <p class="title__tea">tea</p>
    <div class="claims">
      <p class="claims__headline">ALL NATURAL</p>
      <p class="claims__weight">NT WT. 200 G</p>
    </div>
    <div class="badges">
      <span class="badge badge--organic"></span>
      <span class="badge badge--vegan"></span>
      <span class="badge badge--fresh"></span>
    </div>
  </section>

</main>
</body>
</html>
```